Pre-workout label and Super Greens label for Brightmoor Nutrition Supplements

I need a label design for Club Brightmoor's 2 supplements. The first is a Pre-workout. The Pre-workout label needs to be 11.25 x 2.5 inches. This label will go on a black container. The second is a Super-Green. The Super-Green label should be 11.25 x 4.25 inches and will go on a white container. We have been selling these for a few years but the current labels are a little meh. I'd like something trendier and bolder. Must keep the Club Brightmoor branding. All the nurtition data must appear . I attached the current designs so you can know the flavors, nutrtional data etc. Thank you!
Updates

I can upload the Club Brightmoor logo! If anyone can tell me how to do that.

```html
<!DOCTYPE html>
<html lang="en">
<head>
<meta charset="utf-8">
<title>Brightmoor Nutrition – Supplement Labels</title>
<link rel="stylesheet" href="https://fonts.googleapis.com/css2?family=Russo+One&family=Roboto+Condensed:wght@400;700&display=swap">
<style>
  :root {
    --bg: #141414;
    --red-deep: #5a1010;
    --red: #b8191f;
    --red-bright: #e2262b;
    --pink: #f4b4b6;
    --yellow: #f7e21c;
    --grey-dark: #6e6e6e;
    --grey-mid: #9a9a9a;
    --grey-light: #d6d6d6;
    --green: #1f8a3a;
    --green-dark: #136127;
    --ink: #1c1c1c;
    --white: #ffffff;
  }
  * { box-sizing: border-box; margin: 0; padding: 0; }
  html, body { width: 1200px; height: 881px; overflow: hidden; background: var(--bg); }
  body { position: relative; font-family: "Roboto Condensed", sans-serif; }

  .label { position: absolute; overflow: hidden; text-align: center; }
  .label > svg.label-art { position: absolute; inset: 0; width: 100%; height: 100%; }
  .label .layer { position: absolute; left: 0; right: 0; }

  .label--preworkout {
    left: 124px; top: 300px; width: 370px; height: 280px;
    background: radial-gradient(ellipse at 50% 45%, var(--red-bright) 0%, var(--red) 40%, var(--red-deep) 100%);
  }
  .label--supergreen {
    left: 705px; top: 236px; width: 391px; height: 410px;
    background: radial-gradient(ellipse at 50% 45%, var(--grey-light) 0%, var(--grey-mid) 55%, var(--grey-dark) 100%);
  }

  .brand-mark {
    display: flex; align-items: center; justify-content: center; gap: 4px;
    font-family: "Roboto Condensed", sans-serif; font-weight: 700; font-size: 10px; letter-spacing: 1px;
  }
  .brand-mark .square { width: 9px; height: 9px; background: var(--red); }
  .label--preworkout .brand-mark { color: var(--white); }
  .label--supergreen .brand-mark { color: var(--ink); }

  .brand-line {
    display: flex; align-items: center; justify-content: center; gap: 4px;
    font-family: "Roboto Condensed", sans-serif; font-weight: 700; font-size: 13px; letter-spacing: 0.5px;
  }
  .brand-line .rule { width: 26px; height: 7px;
    background: repeating-linear-gradient(to bottom, currentColor 0 1px, transparent 1px 2px); }
  .label--preworkout .brand-line { color: var(--white); }
  .label--supergreen .brand-line { color: var(--ink); font-size: 14px; }

  .product-name { font-family: "Russo One", sans-serif; line-height: 1; letter-spacing: 1px; }
  .label--preworkout .product-name { color: var(--white); font-size: 26px; }
  .label--supergreen .product-name { color: var(--green); font-size: 29px; }

  .flavour {
    display: inline-block; font-weight: 700; letter-spacing: 1.5px; padding: 0 4px; border-radius: 2px;
  }
  .label--preworkout .flavour { color: var(--white); font-size: 9px; border: 1px solid var(--white); }
  .label--supergreen .flavour { color: var(--ink); font-size: 10px; border: 1px solid var(--green); padding: 0 8px; }

  .benefits { display: flex; justify-content: center; }
  .benefit { display: flex; flex-direction: column; align-items: center; }
  .benefit svg { display: block; }
  .label--preworkout .benefits { gap: 14px; }
  .label--preworkout .benefit { width: 54px; }
  .label--preworkout .benefit-title { color: var(--yellow); font-size: 8.5px; margin-top: 4px; }
  .label--preworkout .benefit-note { color: var(--white); font-size: 7px; }
  .label--supergreen .benefits { gap: 30px; }
  .label--supergreen .benefit { width: 60px; }
  .label--supergreen .benefit-title { color: var(--ink); font-size: 10.5px; font-weight: 700; letter-spacing: 0.6px; margin-top: 8px; line-height: 1.25; }
  .label--supergreen .benefit-note { color: var(--ink); font-size: 8px; }

  .footer-row {
    display: flex; justify-content: space-between; font-weight: 700; color: var(--white); letter-spacing: 0.5px;
  }
  .label--preworkout .footer-row { font-size: 7.5px; padding: 0 70px 0 80px; }
  .label--supergreen .footer-row { font-size: 8.5px; padding: 0 70px 0 70px; }
</style>
</head>
<body>

<section class="label label--preworkout" aria-label="Pre-workout label">
  <svg class="label-art" viewBox="0 0 370 280" preserveAspectRatio="none" aria-hidden="true">
    <path d="M15 0 C90 70 260 70 345 0 L345 0 C260 95 90 95 15 0 Z" fill="#f8c9cb" opacity="0.85"/>
    <path d="M15 0 C80 55 270 60 345 0 Z" fill="#c8232a"/>
    <path d="M30 280 C150 215 260 200 345 280 Z" fill="#c8232a"/>
    <path d="M30 280 C150 205 260 190 345 280 C250 215 140 220 30 280 Z" fill="#f8c9cb" opacity="0.8"/>
  </svg>
  <div class="layer" style="top:18px"><div class="brand-mark"><span class="square"></span>BRIGHTMOOR</div></div>
  <div class="layer" style="top:82px"><div class="brand-line"><span class="rule"></span>BRIGHTMOOR NUTRITION<span class="rule"></span></div></div>
  <div class="layer" style="top:103px"><h1 class="product-name">PRE-WORKOUT</h1></div>
  <div class="layer" style="top:138px"><span class="flavour">WATERMELON SUGAR</span></div>
  <div class="layer" style="top:165px">
    <ul class="benefits">
      <li class="benefit">
        <svg width="24" height="28" viewBox="0 0 24 28"><path d="M2 2h20v18l-10 6-10-6z" fill="#fff"/><path d="M4 4h16v15l-8 5-8-5z" fill="var(--red-deep)"/><path d="M13 6l-5 9h4l-2 7 6-10h-4z" fill="var(--yellow)"/></svg>
        <span class="benefit-title">ENERGY*</span><span class="benefit-note">(Caffeine)</span>
      </li>
      <li class="benefit">
        <svg width="24" height="28" viewBox="0 0 24 28"><path d="M2 2h20v18l-10 6-10-6z" fill="#fff"/><path d="M4 4h16v15l-8 5-8-5z" fill="var(--red-deep)"/><path d="M12 6l5 6h-3v8h-4v-8h-3z" fill="var(--yellow)"/></svg>
        <span class="benefit-title">PERFORMANCE*</span><span class="benefit-note">(Beta-alanine)</span>
      </li>
      <li class="benefit">
        <svg width="24" height="28" viewBox="0 0 24 28"><path d="M2 2h20v18l-10 6-10-6z" fill="#fff"/><path d="M4 4h16v15l-8 5-8-5z" fill="var(--red-deep)"/><path d="M6 9h2v8H6zM16 9h2v8h-2zM8 12h8v2H8z" fill="var(--yellow)"/></svg>
        <span class="benefit-title">STRENGTH*</span><span class="benefit-note">(Creatine)</span>
      </li>
    </ul>
  </div>
  <div class="layer" style="top:256px">
    <div class="footer-row"><span>DIETARY SUPPLEMENT</span><span>30 SERVINGS 240g (8.5oz)</span></div>
  </div>
</section>

<section class="label label--supergreen" aria-label="Super Green label">
  <svg class="label-art" viewBox="0 0 391 410" preserveAspectRatio="none" aria-hidden="true">
    <path d="M0 0 C60 140 230 150 391 30 L391 0 Z" fill="#8c8c8c"/>
    <path d="M0 10 C70 130 220 135 380 35 C230 160 60 150 0 30 Z" fill="#f2f2f2"/>
    <path d="M0 410 L0 395 C130 300 250 280 391 335 L391 410 Z" fill="#8c8c8c"/>
    <path d="M0 395 C130 300 250 280 391 335 L391 345 C250 300 130 310 0 400 Z" fill="#f2f2f2"/>
  </svg>
  <div class="layer" style="top:58px"><div class="brand-mark"><span class="square"></span>BRIGHTMOOR</div></div>
  <div class="layer" style="top:146px"><div class="brand-line"><span class="rule"></span>BRIGHTMOOR NUTRITION<span class="rule"></span></div></div>
  <div class="layer" style="top:168px"><h1 class="product-name">SUPER GREEN</h1></div>
  <div class="layer" style="top:206px"><span class="flavour">APPLE CINNAMON</span></div>
  <div class="layer" style="top:236px">
    <ul class="benefits">
      <li class="benefit">
        <svg width="34" height="36" viewBox="0 0 34 36"><path d="M1 1h32v25l-16 9-16-9z" fill="#c0242b"/><path d="M11 13c-4 0-4 7 0 7 3 0 9-7 12-7 4 0 4 7 0 7-3 0-9-7-12-7z" fill="none" stroke="#fff" stroke-width="3"/></svg>
        <span class="benefit-title">DETOX</span><span class="benefit-note">BODY*</span>
      </li>
      <li class="benefit">
        <svg width="34" height="36" viewBox="0 0 34 36"><path d="M1 1h32v25l-16 9-16-9z" fill="#c0242b"/><path d="M15 7v5c5 0 7 4 5 8-2 3-6 2-8 5" fill="none" stroke="#fff" stroke-width="1.5"/></svg>
        <span class="benefit-title">PROMOTE HEALTHY</span><span class="benefit-note">DIGESTION*</span>
      </li>
      <li class="benefit">
        <svg width="34" height="36" viewBox="0 0 34 36"><path d="M1 1h32v25l-16 9-16-9z" fill="#c0242b"/><path d="M17 24l-7-7c-3-3 0-8 4-6l3 2 3-2c4-2 7 3 4 6z" fill="#fff"/></svg>
        <span class="benefit-title">SUPPORT</span><span class="benefit-note">IMMUNITY*</span>
      </li>
    </ul>
  </div>
  <div class="layer" style="top:385px">
    <div class="footer-row"><span>DIETARY SUPPLEMENT</span><span>30 SERVINGS 270g (9.5oz)</span></div>
  </div>
</section>

</body>
</html>
```